Company Website for Vortel Insight, an open source data analytics company focused on relationship and li

I need a company/brand website for our new startup, Vortel Insight LLC. We are a company focused on using life pattern analysis techniques, looking at relationships and how relationships, attributes, and activity cluster to infer aggregate information about individuals and groups. Our focus is on improving the digital advertising market.

We have a company logo which I will upload shortly.

Target Market(s)

Digital Advertising

Number of Pages Required

3 page

Font styles to use
Sans Serif

Requirements
Must have
• An main page, about us, contact page.
Nice to have
• Vortel Insight relies on state of the art analytics applied to a the digital marketing space. While it is heavy in science, we also understand the art of influence. The website should have a scientific edge but also a flair that illustrates our focus on applying the hard science and analytics to influencing the behavior of people.

```html
<!DOCTYPE html>
<html lang="en">
<head>
<meta charset="utf-8">
<title>Vortel Insight</title>
<link rel="stylesheet" href="https://fonts.googleapis.com/css2?family=Poppins:wght@500;600&family=Jost:wght@400;500;600&display=swap">
<style>
:root{
  --orange:#f7931e;
  --orange-soft:#fde3c4;
  --ink:#111111;
  --text:#5c5c5c;
  --muted:#9a9a9a;
  --line:#d9d9d9;
  --paper:#ffffff;
  --panel:#f8f8f8;
  --brand:#1b75bb;
}
*{box-sizing:border-box;margin:0;padding:0}
html,body{width:1200px;height:3180px;overflow:hidden;background:var(--paper)}
body{position:relative;font-family:"Jost",sans-serif;color:var(--text)}
.abs{position:absolute}
h1,h2,h3{font-family:"Poppins",sans-serif;color:var(--ink);font-weight:600}
.btn{position:absolute;background:var(--orange);color:#fff;font-family:"Poppins",sans-serif;font-weight:500;font-size:15px;display:flex;align-items:center;justify-content:center;text-decoration:none}

/* header */
.logo{left:78px;top:26px;font-family:"Jost",sans-serif;font-weight:600;font-size:30px;color:var(--brand);display:flex;align-items:center;gap:10px}
.logo-dot{width:16px;height:16px;border-radius:50%;background:var(--brand)}
.nav{top:46px;display:flex;font-size:15px}
.nav a{position:absolute;white-space:nowrap;color:#fff;text-decoration:none}
.nav a.home{color:var(--ink)}
.join{left:998px;top:36px;width:123px;height:42px;border-radius:21px;background:#fff;color:var(--ink);font-weight:600}

/* hero */
.hero-title{left:78px;top:236px;font-size:28px;line-height:40px;width:420px}
.hero-text{left:78px;top:340px;width:360px;font-size:14px;line-height:26px}
.hero-btn{left:78px;top:426px;width:145px;height:42px}

/* about */
.about-title{left:628px;top:742px;font-size:33px}
.about-text{left:628px;top:806px;width:492px;font-size:14px;line-height:26.5px}
.about-btn{left:625px;top:1000px;width:145px;height:41px}

/* focus */
.focus-title{left:78px;top:1206px;font-size:32px}
.focus-text{left:78px;width:510px;font-size:14px;line-height:26px}
.focus-label{position:absolute;color:#fff;font-family:"Poppins",sans-serif;font-weight:500;font-size:15px;text-align:center;width:200px}

/* blog */
.blog-title{left:0;width:1200px;text-align:center;top:1640px;font-size:33px}
.card{position:absolute;top:1719px;width:322px;height:333px;background:#fff;box-shadow:0 6px 22px rgba(0,0,0,.09)}
.card-media{height:187px}
.card h3{font-size:16px;line-height:26px;margin:20px 22px 0;font-weight:600}
.card-author{display:flex;align-items:center;gap:20px;margin:14px 0 0 24px;font-size:14px;color:var(--muted)}
.avatar{width:40px;height:40px;border-radius:50%;background:linear-gradient(135deg,#c9b3a3,#7d6a60)}

/* contact */
.contact{left:0;top:2116px;width:1200px;height:551px;background:var(--panel);overflow:hidden}
.contact-title{left:0;width:1200px;text-align:center;top:2170px;font-size:33px}
.contact-text{left:0;width:1200px;text-align:center;top:2238px;font-size:14px;line-height:28px}
.field{position:absolute;left:418px;width:364px;height:42px;border:1px solid var(--line);background:#fff;font-size:14px;color:#b3b3b3;padding:10px 12px}
.field.active{border-color:#bdbdbd;color:var(--text)}
.send{left:543px;top:2563px;width:144px;height:42px}

/* info */
.info{position:absolute;top:2730px;width:300px;text-align:center}
.info-icon{width:48px;height:48px;margin:0 auto}
.info h4{font-family:"Jost",sans-serif;color:var(--orange);font-weight:500;font-size:19px;margin-top:8px}
.info p{font-size:14px;line-height:27px;margin-top:4px}
.divider{position:absolute;top:2712px;width:1px;height:170px;background:#e6e6e6}

/* footer */
.footer{left:0;top:2940px;width:1200px;height:240px;background:var(--orange);color:#fff}
.foot-links{position:absolute;top:52px;left:0;width:1200px;display:flex;justify-content:center;gap:26px;font-size:14px}
.foot-rule{position:absolute;left:78px;top:176px;width:1044px;height:1px;background:rgba(255,255,255,.45)}
.copyright{position:absolute;top:195px;width:1200px;text-align:center;font-size:14px}
</style>
</head>
<body>

<!-- hero backdrop -->
<svg class="abs" style="left:0;top:0" width="1200" height="640" viewBox="0 0 1200 640">
  <path d="M720 0H1200V500Q1150 560 1080 610H780Q615 610 615 440V240Q615 140 690 60Z" fill="var(--orange)"/>
</svg>
<div class="abs" role="img" aria-label="Illustration of people gathered around a large phone screen sharing content" style="left:600px;top:290px;width:600px;height:340px;border-radius:30px 30px 0 0;background:linear-gradient(180deg,rgba(108,117,214,.85),rgba(120,220,200,.7))"></div>

<header>
  <div class="abs logo"><span class="logo-dot"></span>Vortel Insight</div>
  <nav class="abs nav">
    <a class="home" style="left:646px">Home</a>
    <a style="left:744px">About Us</a>
    <a style="left:854px">Contact Us</a>
  </nav>
  <a class="btn join">Join Now</a>
</header>

<section>
  <h1 class="abs hero-title">Improving the digital advertising market.</h1>
  <p class="abs hero-text">Lorem Ipsum is simply dummy text of the printing and typesetting industry.</p>
  <a class="btn hero-btn">Contact Now</a>
</section>

<!-- about -->
<section>
  <svg class="abs" style="left:70px;top:740px" width="520" height="320" viewBox="0 0 520 320">
    <rect x="45" y="45" width="170" height="170" rx="30" transform="rotate(45 130 160)" fill="none" stroke="var(--orange)" stroke-width="2"/>
    <rect x="395" y="27" width="84" height="84" rx="16" transform="rotate(45 437 69)" fill="var(--orange)"/>
  </svg>
  <div class="abs" role="img" aria-label="Photo of a woman working on a laptop" style="left:225px;top:792px;width:208px;height:208px;border-radius:36px;transform:rotate(45deg);background:linear-gradient(135deg,#7a6a62,#d7d2cc)"></div>
  <h2 class="abs about-title">About Vortel Insight</h2>
  <p class="abs about-text">Lorem Ipsum is simply dummy text of the printing and typesetting industry. Lorem Ipsum has been the industry's standard dummy text ever since the 1500s, when an unknown printer took a galley of type and scrambled it to make a type specimen book. It has survived not only five centuries, but also the leap into electronic typesetting, remaining essentially unchanged.</p>
  <a class="btn about-btn">Know More</a>
</section>

<!-- company focus -->
<section>
  <h2 class="abs focus-title">Company Focus</h2>
  <p class="abs focus-text" style="top:1280px">Lorem Ipsum is simply dummy text of the printing and typesetting industry. Lorem Ipsum has been the text ever since the 1500s,</p>
  <p class="abs focus-text" style="top:1374px">Lorem Ipsum is simply dummy text of the printing and typesetting industry. Lorem Ipsum has been the industry's standard dummy text ever since the 1500s, when an unknown printer took a galley of type and scrambled it to make a type specimen book.</p>

  <div class="abs" style="left:806px;top:1142px;width:150px;height:150px;border-radius:24px;transform:rotate(45deg);background:var(--orange)"></div>
  <div class="abs" role="img" aria-label="Photo of a business handshake" style="left:689px;top:1262px;width:150px;height:150px;border-radius:24px;transform:rotate(45deg);border:2px solid var(--orange);background:linear-gradient(135deg,#9fb0c4,#3f4f66)"></div>
  <div class="abs" role="img" aria-label="Photo of a team meeting at a whiteboard" style="left:923px;top:1262px;width:150px;height:150px;border-radius:24px;transform:rotate(45deg);border:2px solid var(--orange);background:linear-gradient(135deg,#b9c7d6,#4b5a6d)"></div>
  <div class="abs" role="img" aria-label="Photo of a woman working at a desk" style="left:806px;top:1378px;width:150px;height:150px;border-radius:24px;transform:rotate(45deg);border:2px solid var(--orange);background:linear-gradient(135deg,#c8b9a8,#5d4f45)"></div>
  <div class="focus-label" style="left:781px;top:1253px">Techniques</div>
  <div class="focus-label" style="left:664px;top:1339px">Relationships</div>
  <div class="focus-label" style="left:898px;top:1339px">Activity Cluster</div>
  <div class="focus-label" style="left:781px;top:1455px">Attributes</div>

  <svg class="abs" style="left:0;top:1525px" width="150" height="230" viewBox="0 0 150 230">
    <rect x="20" y="20" width="54" height="54" rx="10" transform="rotate(45 47 47)" fill="var(--orange-soft)" opacity=".8"/>
    <rect x="70" y="66" width="54" height="54" rx="10" transform="rotate(45 97 93)" fill="var(--orange-soft)"/>
    <rect x="-10" y="94" width="54" height="54" rx="10" transform="rotate(45 17 121)" fill="var(--orange-soft)" opacity=".7"/>
    <rect x="-14" y="168" width="54" height="54" rx="10" transform="rotate(45 13 195)" fill="var(--orange-soft)"/>
  </svg>
</section>

<!-- blog -->
<section>
  <h2 class="abs blog-title">Latest Blog</h2>
  <article class="card" style="left:78px">
    <div class="card-media" role="img" aria-label="Photo of a woman thinking at her laptop" style="background:linear-gradient(135deg,#e9e6e2,#8c847d)"></div>
    <h3>Lorem ipsum is simply dummy text of typesetting</h3>
    <div class="card-author"><span class="avatar"></span>Admin Name</div>
  </article>
  <article class="card" style="left:439px">
    <div class="card-media" role="img" aria-label="Photo of a business team posing together" style="background:linear-gradient(135deg,#e4e4e4,#6c6f75)"></div>
    <h3>Lorem ipsum is simply dummy text of typesetting</h3>
    <div class="card-author"><span class="avatar"></span>Admin Name</div>
  </article>
  <article class="card" style="left:799px">
    <div class="card-media" role="img" aria-label="Photo of two colleagues looking at a laptop" style="background:linear-gradient(135deg,#dcdcd6,#5f6a5c)"></div>
    <h3>Lorem ipsum is simply dummy text of typesetting</h3>
    <div class="card-author"><span class="avatar"></span>Admin Name</div>
  </article>
</section>

<!-- contact -->
<section>
  <div class="abs contact">
    <svg class="abs" style="left:1085px;top:170px" width="130" height="250" viewBox="0 0 130 250">
      <rect x="40" y="40" width="160" height="160" rx="30" transform="rotate(45 120 120)" fill="none" stroke="var(--orange)" stroke-width="7"/>
    </svg>
  </div>
  <h2 class="abs contact-title">Contact Us</h2>
  <p class="abs contact-text">Lorem Ipsum is simply dummy text of the printing and typesetting industry.<br>Lorem Ipsum has been the text ever since the 1500s,</p>
  <div class="field active" style="top:2325px">Name*</div>
  <div class="field" style="top:2378px">E-mail*</div>
  <div class="field" style="top:2431px">Phone*</div>
  <div class="field" style="top:2484px;height:70px">Message</div>
  <a class="btn send">Send Now</a>
</section>

<!-- contact info -->
<section>
  <div class="divider" style="left:420px"></div>
  <div class="divider" style="left:780px"></div>
  <div class="info" style="left:90px">
    <svg class="info-icon" viewBox="0 0 48 48"><circle cx="24" cy="24" r="21" fill="none" stroke="var(--orange)" stroke-width="2"/><path d="M17 14l5 1 1 5-3 2q2 5 6 7l2-3 5 1 1 5q-2 3-5 2-12-4-15-16-1-3 3-4z" fill="none" stroke="var(--orange)" stroke-width="2" stroke-linejoin="round"/></svg>
    <h4>Call Us</h4>
    <p>123 456 7890</p>
  </div>
  <div class="info" style="left:450px">
    <svg class="info-icon" viewBox="0 0 48 48"><circle cx="24" cy="24" r="21" fill="none" stroke="var(--orange)" stroke-width="2"/><path d="M24 35s-8-8-8-14a8 8 0 0 1 16 0c0 6-8 14-8 14z" fill="none" stroke="var(--orange)" stroke-width="2"/><circle cx="24" cy="21" r="3" fill="var(--orange)"/></svg>
    <h4>Address</h4>
    <p>123, Lorem ipsum is simply<br>dummy text of typesetting</p>
  </div>
  <div class="info" style="left:810px">
    <svg class="info-icon" viewBox="0 0 48 48"><circle cx="24" cy="24" r="21" fill="var(--orange)"/><rect x="14" y="17" width="20" height="14" rx="1.5" fill="none" stroke="#fff" stroke-width="2"/><path d="M14 18l10 8 10-8" fill="none" stroke="#fff" stroke-width="2"/></svg>
    <h4>E-mail</h4>
    <p>info@vortelinsight.com</p>
  </div>
</section>

<footer class="abs footer">
  <nav class="foot-links"><span>Home</span><span>|</span><span>About Us</span><span>|</span><span>Contact us</span></nav>
  <svg class="abs" style="left:520px;top:104px" width="160" height="44" viewBox="0 0 160 44">
    <rect x="9" y="9" width="26" height="26" rx="4" transform="rotate(45 22 22)" fill="#fff"/>
    <rect x="67" y="9" width="26" height="26" rx="4" transform="rotate(45 80 22)" fill="none" stroke="#fff" stroke-width="2"/>
    <rect x="125" y="9" width="26" height="26" rx="4" transform="rotate(45 138 22)" fill="none" stroke="#fff" stroke-width="2"/>
  </svg>
  <div class="foot-rule"></div>
  <p class="copyright">© Vortel Insight- 2018. All Rights Reserved.</p>
</footer>

</body>
</html>
```